co working space / serviced office/ business centre

Brivlo - brivlo.in, is a very young brand bieng run by 3 young entrepreneurs. We want to be become out of the league company delivering fabulous and beautiful serviced offices in India and abroad. We hire designers who have made spaces across the world. We want to get visiting card design which gives complete fresh look to the people who carries that card, has to be very impactful and should symbolise happy young and energetic brand. should be completely out of the box thinking of international level, should portray global brand image.

Target Market(s)

Startups, (Small, medium and large corporates)

Industry/Entity Type

Business

Contact Information for Business Card

Name, Email, Address, Mobile number, Landline number, website

Colors

Designer to choose colors to be used in the design.

Requirements
Must have
• Nice new shape
Nice to have
• We want creative cuts, different size and impactful brand clarity
Should not have
• Boring and regular design and shape

```html
<!DOCTYPE html>
<html lang="en">
<head>
<meta charset="utf-8">
<title>Brivlo Business Card</title>
<link rel="stylesheet" href="https://fonts.googleapis.com/css2?family=Open+Sans:wght@400;600;700&display=swap">
<style>
  :root {
    --bg: #3a3a3a;
    --red: #e8323c;
    --black: #000000;
    --white: #ffffff;
    --ink: #2b2b2b;
  }
  * { box-sizing: border-box; margin: 0; padding: 0; }
  html, body {
    width: 1200px; height: 864px; overflow: hidden;
    background: var(--bg);
    font-family: "Open Sans", Arial, sans-serif;
  }
  .stage { position: relative; width: 1200px; height: 864px; }
  .card {
    position: absolute; top: 283px;
    width: 520px; height: 297px;
    box-shadow: 0 10px 30px rgba(0,0,0,0.45);
    overflow: hidden;
  }
  .card--front { left: 40px; background: var(--black); }
  .card--back { left: 640px; background: var(--white); }

  .brand {
    display: flex; align-items: center; gap: 10px;
    color: var(--red); font-weight: 700; letter-spacing: 3px;
  }
  .brand__dot { border-radius: 50%; background: var(--red); flex: none; }

  .card--front .brand {
    position: absolute; left: 0; right: 0; top: 96px;
    justify-content: center; font-size: 52px;
  }
  .card--front .brand__dot { width: 26px; height: 26px; }
  .front__rule {
    position: absolute; left: 150px; width: 220px; top: 176px;
    height: 3px; background: var(--red);
  }
  .front__web {
    position: absolute; left: 0; right: 0; top: 212px;
    text-align: center; color: var(--white); font-size: 15px; font-weight: 600;
  }

  .card--back .brand {
    position: absolute; left: 30px; top: 36px; font-size: 34px;
  }
  .card--back .brand__dot { width: 18px; height: 18px; }
  .back__rule {
    position: absolute; left: 30px; width: 178px; top: 90px;
    height: 2px; background: var(--red);
  }
  .band {
    position: absolute; left: 0; top: 122px; width: 486px; height: 54px;
    background: var(--red); color: var(--white);
    padding: 6px 0 0 32px;
  }
  .band__tab {
    position: absolute; right: 0; top: 122px; width: 30px; height: 34px;
    background: var(--black);
  }
  .person__name { font-size: 20px; font-weight: 700; line-height: 1.2; }
  .person__role { font-size: 13px; line-height: 1.3; }

  .contacts {
    position: absolute; left: 32px; top: 190px; list-style: none;
    color: var(--ink); font-size: 14px;
  }
  .contacts li { display: flex; align-items: center; gap: 8px; height: 21px; }
  .contacts svg { width: 12px; height: 12px; flex: none; }

  .address {
    position: absolute; right: 32px; top: 210px;
    text-align: right; color: var(--ink); font-size: 14px; line-height: 1.5;
  }
</style>
</head>
<body>
<main class="stage">
  <section class="card card--front" aria-label="Card front">
    <div class="brand"><span class="brand__dot"></span><span class="brand__name">BRIVLO</span></div>
    <div class="front__rule"></div>
    <p class="front__web">www.brivlo.in</p>
  </section>

  <section class="card card--back" aria-label="Card back">
    <div class="brand"><span class="brand__dot"></span><span class="brand__name">BRIVLO</span></div>
    <div class="back__rule"></div>

    <div class="band">
      <p class="person__name">Rohan Kapoor</p>
      <p class="person__role">President</p>
    </div>
    <div class="band__tab"></div>

    <ul class="contacts">
      <li>
        <svg viewBox="0 0 24 24" fill="#e8323c"><path d="M6.6 10.8a15 15 0 0 0 6.6 6.6l2.2-2.2c.3-.3.7-.4 1-.2 1.1.4 2.3.6 3.6.6.6 0 1 .4 1 1V20c0 .6-.4 1-1 1A17 17 0 0 1 3 4c0-.6.4-1 1-1h3.5c.6 0 1 .4 1 1 0 1.3.2 2.5.6 3.6.1.3 0 .7-.2 1z"/></svg>
        01 012-345-6789
      </li>
      <li>
        <svg viewBox="0 0 24 24" fill="none" stroke="#e8323c" stroke-width="3"><rect x="6" y="2" width="12" height="20" rx="2"/></svg>
        01 012-345-6780
      </li>
      <li>
        <svg viewBox="0 0 24 24" fill="#e8323c"><path d="M2 5h20v14H2z"/><path d="M2 5l10 8 10-8" fill="none" stroke="#fff" stroke-width="2"/></svg>
        info@yourwebsite.com
      </li>
      <li>
        <svg viewBox="0 0 24 24" fill="none" stroke="#e8323c" stroke-width="2.5"><circle cx="12" cy="12" r="10"/><path d="M2 12h20M12 2c3 3 3 17 0 20M12 2c-3 3-3 17 0 20"/></svg>
        www.brivlo.in
      </li>
    </ul>

    <p class="address">Street Name, Suite 100<br>State, Zip Code, Country</p>
  </section>
</main>
</body>
</html>
```